This is a label for a new sake made in Japan imported into Aust

This will be a bottle label for a new sake imported into Australia. The hero of the label is the Velmora. We have joined the "O" meaning great in Japanese and used sake with "Z" to have Velmora with the play on words using Oz as in our slang for Aussie. A modern label with a Japanese take is key. This is a premium sake made in Japan for the Australian market.
The "Tall Casks" up the top is the name of the company, we have yet to design a logo for the company.

Target Market(s)

Alcohol

Logo Text

Velmora

Font styles to use
Serif

Requirements
Must have
• easy to read, with a hint of Japanese origin
Should not have
• too busy

```html
<!DOCTYPE html>
<html lang="en">
<head>
<meta charset="utf-8">
<title>Velmora – Premium Japanese Sake label presentation</title>
<link rel="stylesheet" href="https://fonts.googleapis.com/css2?family=Libre+Baskerville:wght@400;700&family=Source+Sans+3:wght@400;600&display=swap">
<style>
  :root {
    --paper: #ffffff;
    --ink: #111111;
    --red: #c8181e;
    --red-soft: #d23a3f;
    --frame: #9a9a9a;
    --caption: #8a8a8a;
    --ceramic-light: #f4f4f4;
    --ceramic-dark: #d4d4d4;
    --glass-light: #f7f9f9;
    --glass-dark: #dbe1e1;
  }
  * { box-sizing: border-box; margin: 0; padding: 0; }
  html, body { width: 847px; height: 1200px; overflow: hidden; background: var(--paper); }
  .sheet { position: relative; width: 847px; height: 1200px; background: var(--paper); font-family: "Libre Baskerville", Georgia, serif; color: var(--ink); }

  .legend { position: absolute; display: flex; align-items: flex-start; gap: 10px; }
  .legend-dot { width: 26px; height: 26px; border-radius: 50%; background: var(--red); flex: none; margin-top: 2px; }
  .legend-title { font-size: 17px; line-height: 1.2; }
  .legend-note { font-size: 13px; line-height: 1.3; }
  .legend--bird { left: 56px; top: 12px; }
  .legend--mark { left: 494px; top: 1140px; }

  .label { position: absolute; border: 1.5px solid var(--frame); background: var(--paper); display: flex; flex-direction: column; align-items: center; text-align: center; }
  .label--bird { left: 62px; top: 93px; width: 455px; height: 452px; padding-top: 36px; }
  .label--mark { left: 446px; top: 740px; width: 372px; height: 375px; padding-top: 30px; }

  .company { font-weight: 700; font-size: 30px; letter-spacing: 0.5px; }
  .label--mark .company { font-size: 25px; }
  .bird-art { width: 150px; height: 150px; background: linear-gradient(160deg, var(--red-soft), var(--red)); border-radius: 6px; }
  .label--bird .bird-art { margin-top: 22px; }
  .brand-name { font-weight: 700; color: var(--ink); letter-spacing: 3px; text-transform: uppercase; }
  .label--bird .brand-name { font-size: 64px; margin-top: 16px; }
  .label--mark .brand-name { font-size: 54px; margin-top: 14px; }
  .brand-dot { width: 70px; height: 70px; border-radius: 50%; background: var(--red); margin-top: 26px; }
  .tagline { font-weight: 400; font-size: 27px; line-height: 1.4; }
  .label--bird .tagline { margin-top: 30px; }
  .label--mark .tagline { font-size: 24px; margin-top: 26px; }

  .bottle { position: absolute; }
  .bottle-fill { position: absolute; inset: 0; border-radius: 10px; }
  .bottle-fill--ceramic { background: linear-gradient(90deg, var(--ceramic-dark), var(--ceramic-light) 45%, var(--ceramic-dark)); }
  .bottle-fill--glass { background: linear-gradient(90deg, var(--glass-dark), var(--glass-light) 50%, var(--glass-dark)); }
  .bottle-text { position: absolute; left: 0; right: 0; text-align: center; color: var(--ink); }
  .bottle-company { font-weight: 700; font-size: 9px; }
  .bottle-brand { font-weight: 700; letter-spacing: 1px; text-transform: uppercase; }
  .bottle-tagline { font-size: 10px; line-height: 1.3; }
  .bottle-bird { position: absolute; left: 50%; transform: translateX(-50%); background: linear-gradient(160deg, var(--red-soft), var(--red)); border-radius: 4px; }
  .bottle-dot { position: absolute; left: 50%; transform: translateX(-50%); border-radius: 50%; background: var(--red); }

  .caption { position: absolute; font-family: "Source Sans 3", Arial, sans-serif; font-size: 10px; letter-spacing: 0.6px; color: var(--caption); text-transform: uppercase; white-space: nowrap; }
</style>
</head>
<body>
<main class="sheet">

  <div class="legend legend--bird">
    <span class="legend-dot" aria-hidden="true"></span>
    <div>
      <p class="legend-title">Cassowary</p>
      <p class="legend-note">Large Bird (northeastern Australia)</p>
    </div>
  </div>

  <section class="label label--bird" aria-label="Label option one">
    <p class="company">Tall Casks</p>
    <div class="bird-art" role="img" aria-label="Red cassowary illustration"></div>
    <p class="brand-name">Velmora</p>
    <p class="tagline">Premium Japanese<br>Sake</p>
  </section>

  <div class="bottle" style="left:545px; top:28px; width:138px; height:537px;">
    <div class="bottle-fill bottle-fill--ceramic" role="img" aria-label="White ceramic sake bottle mockup"></div>
    <p class="bottle-text bottle-company" style="top:12px;">Tall Casks</p>
    <div class="bottle-bird" role="img" aria-label="Red cassowary illustration" style="top:340px; width:56px; height:90px;"></div>
    <p class="bottle-text bottle-brand" style="top:444px; font-size:20px;">Velmora</p>
    <p class="bottle-text bottle-tagline" style="top:480px;">Premium Japanese<br>Sake</p>
  </div>
  <p class="caption" style="left:565px; top:582px;">Ceramic bottle</p>

  <div class="bottle" style="left:700px; top:155px; width:118px; height:425px;">
    <div class="bottle-fill bottle-fill--glass" role="img" aria-label="Clear glass sake bottle mockup"></div>
    <div class="bottle-bird" role="img" aria-label="Red cassowary illustration" style="top:150px; width:46px; height:60px;"></div>
    <p class="bottle-text bottle-brand" style="top:222px; font-size:17px;">Velmora</p>
    <p class="bottle-text bottle-tagline" style="top:254px;">Premium Japanese<br>Sake</p>
  </div>
  <p class="caption" style="left:720px; top:598px;">Crestline King</p>

  <div class="bottle" style="left:62px; top:705px; width:215px; height:425px;">
    <div class="bottle-fill bottle-fill--glass" role="img" aria-label="Square clear glass sake bottle mockup"></div>
    <p class="bottle-text bottle-company" style="top:138px;">Tall Casks</p>
    <span class="bottle-dot" aria-hidden="true" style="top:168px; width:34px; height:34px;"></span>
    <p class="bottle-text bottle-brand" style="top:214px; font-size:22px;">Velmora</p>
    <p class="bottle-text bottle-tagline" style="top:250px;">Premium Japanese<br>Sake</p>
  </div>
  <p class="caption" style="left:110px; top:1140px;">Crestline Quartz</p>

  <div class="bottle" style="left:291px; top:663px; width:138px; height:494px;">
    <div class="bottle-fill bottle-fill--ceramic" role="img" aria-label="White ceramic sake bottle mockup"></div>
    <p class="bottle-text bottle-company" style="top:12px;">Tall Casks</p>
    <span class="bottle-dot" aria-hidden="true" style="top:252px; width:34px; height:34px;"></span>
    <p class="bottle-text bottle-brand" style="top:300px; font-size:20px;">Velmora</p>
    <p class="bottle-text bottle-tagline" style="top:336px;">Premium Japanese<br>Sake</p>
  </div>

  <section class="label label--mark" aria-label="Label option two">
    <p class="company">Tall Casks</p>
    <span class="brand-dot" aria-hidden="true"></span>
    <p class="brand-name">Velmora</p>
    <p class="tagline">Premium Japanese<br>Sake</p>
  </section>

  <div class="legend legend--mark">
    <span class="legend-dot" aria-hidden="true"></span>
    <div>
      <p class="legend-note">Dai (Kanji for Big)</p>
      <p class="legend-note">and Mount Fuji</p>
    </div>
  </div>

</main>
</body>
</html>
```